Carpet Cleaning Business Sesighn

Brio-Kleen is a carpet cleaning company we do more than carpet cleaning, carpet cleaning, upholstery cleaning, tile and grout cleaning, wood floor cleaning & refinishing, maid service, air duct cleaning, pet odor and urine removal, water restoration and carpet repair. we need a business card design for our company to match our web site http://www.brio-kleen-carpet-cleaning.example we also need our logo on our card something like our web site, colors are red, gray, black like our web site. I want the logo to pop like our web site also.
Industry/Entity Type
Business
Contact Information for Business Card
Brio-Kleen Carpet Cleaning
Martin Odsway
7182 Bellcroft Rd Marlow Falls, OH 45871
President
Office 555 730-1962
Cell 555 284-6157
Email Martin@Brio-Kleen-Carpet-Cleaning.example
www.brio-kleen-carpet-cleaning.example

```html
<!DOCTYPE html>
<html lang="en">
<head>
<meta charset="utf-8">
<title>Brio-Kleen Carpet Cleaning — Business Card</title>
<link rel="stylesheet" href="https://fonts.googleapis.com/css2?family=Open+Sans:wght@400;600;700&display=swap">
<style>
  :root {
    --page-bg: #ecebe8;
    --red-light: #9c1d21;
    --red-mid: #861619;
    --red-dark: #5f0d10;
    --band-red: #6a0f12;
    --white: #ffffff;
    --paper-top: #ffffff;
    --paper-bottom: #e4e4e4;
    --steel-light: #c9cbce;
    --steel-dark: #4a4c50;
    --text-soft: #e9d6d6;
    --icon-ink: #6a0f12;
  }
  * { box-sizing: border-box; margin: 0; padding: 0; }
  html, body {
    width: 1200px; height: 900px; overflow: hidden;
    background: var(--page-bg);
    font-family: "Open Sans", "Myriad Pro", Arial, sans-serif;
  }
  .sheet {
    width: 1200px; height: 900px;
    display: flex; flex-direction: column; align-items: center; justify-content: center;
    gap: 44px;
  }
  .card {
    width: 600px; height: 343px;
    position: relative; overflow: hidden;
    box-shadow: 0 6px 18px rgba(0,0,0,.18);
  }
  /* Front */
  .card--front {
    background: radial-gradient(ellipse at 50% 40%, var(--red-light) 0%, var(--red-mid) 45%, var(--red-dark) 100%);
    display: flex; align-items: center; justify-content: center;
  }
  .brand { display: flex; align-items: center; gap: 14px; }
  .brand__dot { width: 22px; height: 22px; border-radius: 50%; }
  .brand__name { font-weight: 700; font-size: 52px; letter-spacing: .5px; }
  .card--front .brand__name { color: var(--steel-light); }
  .card--front .brand__dot { background: var(--steel-light); }
  /* Back */
  .card--back {
    background: linear-gradient(180deg, var(--paper-top) 0%, var(--paper-bottom) 54%);
  }
  .card--back .brand {
    position: absolute; top: 46px; left: 0; right: 0; justify-content: center;
  }
  .card--back .brand__name { font-size: 46px; color: var(--steel-dark); }
  .card--back .brand__dot { background: var(--band-red); width: 20px; height: 20px; }
  .band {
    position: absolute; left: 0; right: 0; top: 183px; bottom: 0;
    background: var(--band-red);
    display: flex; padding: 20px 0 0;
  }
  .person {
    width: 268px; padding-right: 16px; text-align: right; color: var(--white);
    flex: none;
  }
  .person__name { font-size: 25px; font-weight: 400; line-height: 1.1; white-space: nowrap; }
  .person__title { font-size: 15px; color: var(--text-soft); margin-top: 2px; }
  .person__address { font-size: 16px; line-height: 1.3; margin-top: 18px; white-space: nowrap; }
  .contacts { list-style: none; padding-left: 4px; }
  .contacts li {
    display: flex; align-items: center; gap: 9px;
    color: var(--white); font-size: 13px; line-height: 1; height: 22px;
    white-space: nowrap;
  }
  .icon {
    width: 16px; height: 16px; border-radius: 3px;
    background: var(--white); display: flex; align-items: center; justify-content: center;
    flex: none;
  }
  .icon svg { width: 11px; height: 11px; fill: var(--icon-ink); }
</style>
</head>
<body>
<main class="sheet">

  <section class="card card--front" aria-label="Card front">
    <div class="brand">
      <span class="brand__dot"></span>
      <span class="brand__name">Brio-Kleen</span>
    </div>
  </section>

  <section class="card card--back" aria-label="Card back">
    <div class="brand">
      <span class="brand__dot"></span>
      <span class="brand__name">Brio-Kleen</span>
    </div>

    <div class="band">
      <div class="person">
        <p class="person__name">Martin Odsway</p>
        <p class="person__title">President</p>
        <p class="person__address">7182 Bellcroft Rd<br>Marlow Falls, OH 45871</p>
      </div>

      <ul class="contacts">
        <li>
          <span class="icon"><svg viewBox="0 0 12 12"><path d="M1 4c0-2 2-3 5-3s5 1 5 3v1H8V4H4v1H1zM3 6h6l2 4H1z"/></svg></span>
          555 730-1962
        </li>
        <li>
          <span class="icon"><svg viewBox="0 0 12 12"><path d="M3 0h6v12H3zM4 1.5v8h4v-8z"/></svg></span>
          555 284-6157
        </li>
        <li>
          <span class="icon"><svg viewBox="0 0 12 12"><path d="M0 2h12v8H0zM1 3l5 4 5-4v-.2H1z"/></svg></span>
          Martin@Brio-Kleen-Carpet-Cleaning.example
        </li>
        <li>
          <span class="icon"><svg viewBox="0 0 12 12"><path d="M5 3L7 1a2.5 2.5 0 0 1 4 4L9 7 8 6l2-2a1 1 0 0 0-2-2L6 4zM7 9l-2 2a2.5 2.5 0 0 1-4-4l2-2 1 1-2 2a1 1 0 0 0 2 2l2-2zM3.5 7.5l4-4 1 1-4 4z"/></svg></span>
          www.brio-kleen-carpet-cleaning.example
        </li>
      </ul>
    </div>
  </section>

</main>
</body>
</html>
```